We specialize in pizza, pasta and salads and are now offering TAKE & BAKE and GRAB & GO ...

Looking for either a 8.5" x 11" or similar for a instore display. WILL BE ON A SWIVELING HOLDER to catch customers attention.

**THIS IS A DOUBLE SIDED PRINT**

ONE SIDE will consist of WHAT'S FOR DINNER TONIGHT? and the following:
* Take & Bake"
* "Baked Pasta"
* Freshly made in house
* Lasagna
$13.50
- please include attached closeup picture and logo

THE OTHER SIDE will consist of
mini charcutier board.
* snack size charcutier delight *
* Enjoy the flavors of gourmet snacking, all in one convenient box!

PRICE $8.99

Winning design will be commissioned to design labels for "grab and go" for take and bake pasta, charcuterie box, pasta salads, candy etc.

Thank you and please do not hesitate to ask any questions.

www.calderipizza.ca
www.fernloop.ca
Logo to be interchanged as they are affiliated meaning FernLoop is a brand within Calderi pizza.

Target Market(s)

our target market is customers who have already entered our business. This is to upsel

Industry/Entity Type

We are in a self serve enviroment and target business people

Requirements
Must have
• must be clean and catchy. We are located in a professional business community.
Nice to have
• Must be appealing, appetizing and utilize our website colors
Should not have
• should not have any carton drawings and not be cluttered (busy)

```html
<!DOCTYPE html>
<html lang="en">
<head>
<meta charset="utf-8">
<title>Calderi pizza – Take &amp; Bake display</title>
<link rel="stylesheet" href="https://fonts.googleapis.com/css2?family=Jost:wght@400;500;700;800&display=swap">
<style>
  :root{
    --brand-red:#ac3024;
    --paper:#ffffff;
    --light-band:#ebebeb;
    --ink:#1f1d22;
    --stage:#8d8d8d;
    --rule:#d27a70;
  }
  *{margin:0;padding:0;box-sizing:border-box}
  html,body{width:1200px;height:1200px;overflow:hidden}
  body{background:var(--stage);font-family:"Jost",sans-serif;position:relative}

  .poster{position:absolute;top:250px;width:540px;height:699px;overflow:hidden;background:var(--brand-red);box-shadow:4px 5px 6px rgba(0,0,0,.35)}
  .poster--pasta{left:40px}
  .poster--board{left:620px}

  .top-band{position:absolute;left:0;top:0;width:100%;height:315px;background:var(--light-band)}

  .brand{position:absolute;top:34px;left:0;width:100%;display:flex;justify-content:center;align-items:center;gap:10px}
  .brand__dot{width:18px;height:18px;border-radius:50%;background:var(--brand-red)}
  .brand__name{font-size:30px;font-weight:400;letter-spacing:1px;color:var(--ink);line-height:1}

  .photo{position:absolute;border-radius:50%;border:3px solid var(--ink)}
  .photo--pasta{left:86px;top:96px;width:378px;height:378px;
    background:radial-gradient(circle at 55% 50%,#efd9a0 0%,#e6c47d 38%,#f4f1ec 55%,#1d2436 72%,#2b2a2a 100%)}
  .photo--board{left:81px;top:19px;width:370px;height:370px;
    background:radial-gradient(circle at 50% 52%,#d79a5c 0%,#c0674a 30%,#8c6a4a 58%,#d8d6d2 74%,#e9e7e4 100%)}

  .pointer{position:absolute;left:0;top:0}

  .price{position:absolute;border-radius:50%;display:flex;flex-direction:column;align-items:center;justify-content:center;color:var(--paper);line-height:1.05}
  .price--pasta{left:360px;top:106px;width:112px;height:112px;background:var(--brand-red);border:3px solid var(--paper);box-shadow:0 0 0 3px var(--brand-red);font-size:24px;font-weight:500}
  .price--board{left:378px;top:238px;width:110px;height:110px;background:var(--ink);font-size:22px;font-weight:500}
  .price__label{font-weight:800;font-size:21px}

  .headline-intro{position:absolute;top:500px;width:100%;text-align:center;color:var(--paper);font-size:29px;font-weight:400;line-height:1}
  .headline-intro strong{font-weight:700}
  .headline-main{position:absolute;top:542px;width:100%;text-align:center;color:var(--paper);font-size:66px;font-weight:800;letter-spacing:1px;line-height:1}

  .tag-row{position:absolute;top:622px;width:100%;display:flex;align-items:center;justify-content:center;gap:24px}
  .tag-row__rule{width:88px;height:1px;background:var(--rule)}
  .tag{background:var(--paper);color:var(--brand-red);font-size:19px;font-weight:500;padding:2px 9px;line-height:1.3}

  .board-title{position:absolute;top:420px;width:100%;text-align:center;color:var(--paper);font-size:29px;font-weight:400;letter-spacing:.5px;line-height:1}
  .board-enjoy{position:absolute;top:456px;width:100%;text-align:center;color:var(--paper);font-size:100px;font-weight:400;letter-spacing:2px;line-height:1}
  .board-copy{position:absolute;top:556px;width:100%;text-align:center;color:var(--paper);font-size:28px;font-weight:400;line-height:1.25;letter-spacing:.5px}
  .board-tag{position:absolute;top:634px;left:0;width:100%;display:flex;justify-content:center}
  .board-tag .tag{font-size:24px;font-weight:400;padding:0 7px}
</style>
</head>
<body>

<section class="poster poster--pasta">
  <div class="top-band"></div>
  <div class="brand"><span class="brand__dot"></span><span class="brand__name">CALDERI PIZZA</span></div>
  <div class="photo photo--pasta" role="img" aria-label="Close-up of baked pasta with cherry tomatoes and herbs in a white baking dish"></div>
  <svg class="pointer" width="540" height="300" viewBox="0 0 540 300" aria-hidden="true">
    <polygon points="79,160 130,102 193,205" fill="var(--brand-red)" stroke="var(--paper)" stroke-width="3" stroke-linejoin="miter"/>
  </svg>
  <div class="price price--pasta">$13.50</div>
  <p class="headline-intro">WHAT'S FOR DINNER <strong>TONIGHT?</strong></p>
  <h1 class="headline-main">BAKED PASTA</h1>
  <div class="tag-row"><span class="tag-row__rule"></span><span class="tag">Freshly made in house</span><span class="tag-row__rule"></span></div>
</section>

<section class="poster poster--board">
  <div class="photo photo--board" role="img" aria-label="Mini charcuterie board with grapes, cheese, salami, crackers and nuts"></div>
  <div class="price price--board"><span class="price__label">PRICE</span><span>$8.99</span></div>
  <p class="board-title">Mini charcutier board.</p>
  <h1 class="board-enjoy">ENJOY</h1>
  <p class="board-copy">the flavors of gourmet snacking,<br>all in one convenient box!</p>
  <div class="board-tag"><span class="tag">snack size charcutier delight</span></div>
</section>

</body>
</html>
```